Committee to Elect Tall Ned Marsh County Commissioner District 1

I need a patriotic Background with Bold Red White and Blue Colors with a steel'ish look. The Front will say "Vote Tall Ned Marsh County Commissioner" With an Emphasis on the name "Marsh" The back needs to be simple color that allows for readable lines. It will have my website, phone, email and facebook links on the back and in small but readable print on the bottom it will say "Paid for by the Committe to Elect Tall Ned Marsh County Commissiner"

```html
<!DOCTYPE html>
<html lang="en">
<head>
<meta charset="utf-8">
<title>Tall Ned Marsh – County Commissioner Card</title>
<link href="https://fonts.googleapis.com/css2?family=Montserrat:wght@400;500;600;700&display=swap" rel="stylesheet">
<style>
  :root {
    --stage-grey: #b3b3b3;
    --card-white: #ffffff;
    --flag-red: #b22234;
    --flag-navy: #3c3b6e;
    --ink-dark: #333333;
    --ink-black: #111111;
  }
  * { margin: 0; padding: 0; box-sizing: border-box; }
  html, body {
    width: 1000px; height: 1200px; overflow: hidden;
    background: var(--stage-grey);
    font-family: "Montserrat", Arial, sans-serif;
  }
  .stage { position: relative; width: 1000px; height: 1200px; }
  .card {
    position: absolute; left: 51px; width: 899px; height: 539px;
    background: var(--card-white); overflow: hidden;
  }
  .card--front { top: 43px; }
  .card--back { top: 617px; }
  .band { position: absolute; left: 0; width: 100%; height: 49px; }
  .band--top { top: 0; background: var(--flag-red); }
  .band--bottom { bottom: 0; background: var(--flag-navy); }

  .headline {
    position: absolute; top: 152px; left: 0; width: 100%;
    text-align: center; text-transform: uppercase;
  }
  .headline__vote {
    display: inline-block; width: 222px; height: 60px;
    background: var(--flag-navy); color: var(--card-white);
    font-weight: 500; font-size: 50px; line-height: 62px; letter-spacing: 2px;
  }
  .headline__first {
    color: var(--flag-red); font-weight: 600; font-size: 52px;
    line-height: 54px; margin-top: 8px;
  }
  .headline__last {
    color: var(--flag-navy); font-weight: 700; font-size: 66px;
    line-height: 64px;
  }
  .headline__office {
    color: var(--flag-red); font-weight: 600; font-size: 34px;
    line-height: 40px; margin-top: 12px;
  }

  .contact { position: absolute; left: 54px; top: 143px; color: var(--ink-dark); }
  .contact__name { font-weight: 600; font-size: 30px; line-height: 36px; }
  .contact__role { font-weight: 400; font-size: 29px; line-height: 36px; }
  .contact__list { list-style: none; margin-top: 16px; }
  .contact__item {
    display: flex; align-items: center; height: 43px;
    font-size: 27px; font-weight: 400; color: var(--ink-black);
  }
  .contact__icon { width: 28px; height: 28px; margin-right: 15px; flex: none; }

  .disclaimer {
    position: absolute; left: 0; width: 100%; top: 446px;
    text-align: center; font-weight: 600; font-size: 20.5px; color: var(--ink-black);
  }
</style>
</head>
<body>
<main class="stage">
  <section class="card card--front">
    <div class="band band--top"></div>
    <div class="headline">
      <div class="headline__vote">Vote</div>
      <div class="headline__first">Tall Ned</div>
      <div class="headline__last">Marsh</div>
      <div class="headline__office">County Commissioner</div>
    </div>
    <div class="band band--bottom"></div>
  </section>

  <section class="card card--back">
    <div class="band band--top"></div>
    <div class="contact">
      <div class="contact__name">Your Name</div>
      <div class="contact__role">Manager</div>
      <ul class="contact__list">
        <li class="contact__item">
          <svg class="contact__icon" viewBox="0 0 28 28" aria-hidden="true">
            <rect width="28" height="28" rx="3" fill="#3c3b6e"/>
            <path d="M9 7c1-.6 2-.5 2.4.3l1.3 2.6c.3.7 0 1.3-.6 1.7l-.8.5c.7 1.8 2 3.2 3.6 4l.6-.8c.4-.6 1.1-.8 1.7-.5l2.6 1.3c.8.4.9 1.5.2 2.4-.9 1.2-2.3 1.7-3.8 1.1C11.8 18.4 9.2 15.7 7.9 11.3 7.5 9.6 7.9 7.8 9 7z" fill="#fff"/>
          </svg>
          123 444 555
        </li>
        <li class="contact__item">
          <svg class="contact__icon" viewBox="0 0 28 28" aria-hidden="true">
            <rect width="28" height="28" rx="3" fill="#3c3b6e"/>
            <rect x="6" y="8.5" width="16" height="11" fill="none" stroke="#fff" stroke-width="1.6"/>
            <path d="M6 8.5l8 6.5 8-6.5M6 19.5l6-5M22 19.5l-6-5" fill="none" stroke="#fff" stroke-width="1.4"/>
          </svg>
          info@yourname.com
        </li>
        <li class="contact__item">
          <svg class="contact__icon" viewBox="0 0 28 28" aria-hidden="true">
            <rect width="28" height="28" rx="3" fill="#3c3b6e"/>
            <g fill="none" stroke="#fff" stroke-width="1.4">
              <circle cx="14" cy="14" r="7.5"/>
              <ellipse cx="14" cy="14" rx="3.2" ry="7.5"/>
              <path d="M6.5 14h15M8 10h12M8 18h12"/>
            </g>
          </svg>
          www.yourname.com
        </li>
        <li class="contact__item">
          <svg class="contact__icon" viewBox="0 0 28 28" aria-hidden="true">
            <rect width="28" height="28" rx="3" fill="#3c3b6e"/>
          </svg>
          socialpage.com/yourname.com
        </li>
      </ul>
    </div>
    <p class="disclaimer">Paid for by the Committe to Elect Tall Ned Marsh County Commissiner</p>
    <div class="band band--bottom"></div>
  </section>
</main>
</body>
</html>
```